Helicopter Company - Rotavia Sweden

I need a new design and implementation of a webpage. We rent helicopters and are also starting a school. We havre started a wordpress but the page is very ugly. Need a complete update. Logo exist already. We also have some pictures of helicotopers. We are open for all designs but it is important that it looks professionel, is eassy to update and will give an impression och structure and dicipline.
Updates

Target Market(s)

Customers that what to get a certificate to fly. It is expensive so it’s either people with a lot of money or people with a big dream. It is very serious business.

Industry/Entity Type

www.rotavia-demo.se

Coding

Coded - Design and coding required

Number of Pages Required

4 page

Font styles to use
Sans Serif

Colors
0054AA
0677BA
7BADD7
CADEEF
E8F1F8

Requirements
Must have
• A easy page the gives a feeling of seriousness and

```html
<!DOCTYPE html>
<html lang="sv">
<head>
<meta charset="utf-8">
<title>Rotavia Sweden – Hyr Din Helikopter</title>
<link href="https://fonts.googleapis.com/css2?family=Cabin:wght@400;500;600&family=Montserrat:wght@400;500;600&display=swap" rel="stylesheet">
<style>
:root{
  --navy:#0c1444;
  --navy-2:#1d2352;
  --ink:#111a3a;
  --text:#5d6378;
  --blue:#0677BA;
  --blue-dark:#0054AA;
  --blue-mid:#7BADD7;
  --blue-light:#CADEEF;
  --page:#F5F7FC;
  --frame:#e3e3e3;
  --white:#ffffff;
  --head:'Cabin',sans-serif;
  --body:'Montserrat',sans-serif;
}
*{box-sizing:border-box;margin:0;padding:0}
html,body{width:1200px;height:4286px;overflow:hidden}
body{background:var(--frame);font-family:var(--body);color:var(--text);position:relative}
.page{position:absolute;left:120px;top:10px;width:960px;height:4266px;background:var(--page);overflow:hidden}
.abs{position:absolute}
a{text-decoration:none;color:inherit}

/* header */
.header{left:0;top:0;width:960px;height:80px;background:var(--white)}
.brand{left:75px;top:26px;font-family:var(--head);font-weight:500;font-size:26px;letter-spacing:3px;color:var(--ink);display:flex;align-items:center;gap:10px}
.brand .dot{width:10px;height:10px;border-radius:50%;background:var(--ink)}
.nav{left:313px;top:34px;display:flex;gap:36px;font-size:12px;font-weight:500;color:var(--ink)}
.callbox{left:680px;top:0;width:280px;height:80px}
.callbox .txt{left:118px;top:24px;color:var(--white);font-size:11px;line-height:17px}
.icon-circle{width:30px;height:30px;border-radius:50%;background:var(--white);display:flex;align-items:center;justify-content:center}

/* hero */
.hero{left:0;top:80px;width:960px;height:602px;background:linear-gradient(180deg,#1f5fb3 0%,#3d83d1 35%,#8fb8e0 70%,#b7b18a 88%,#0c1444 100%)}
.hero-photo{left:420px;top:0;width:540px;height:540px;background:radial-gradient(ellipse at 60% 60%,#1a2236 0%,#24345a 35%,rgba(60,110,190,0) 70%)}
.eyebrow{left:95px;top:195px;color:var(--white);font-size:13px;font-family:var(--head);border-bottom:1px solid var(--white);padding-bottom:3px}
.hero h1{left:95px;top:225px;width:380px;color:var(--white);font-family:var(--head);font-weight:500;font-size:40px;line-height:52px}
.hero p{left:97px;top:351px;width:330px;color:var(--blue-light);font-size:10px;line-height:13px}
.btn-pill{left:95px;top:422px;height:26px;padding:0 13px;border-radius:13px;background:var(--navy);color:var(--white);font-size:11px;line-height:26px;font-weight:500}

.feature-card{left:125px;top:609px;width:737px;height:176px;background:var(--white);border-radius:8px;box-shadow:0 6px 18px rgba(12,20,68,.18)}
.feature{top:24px;width:300px}
.feature h3{font-family:var(--head);font-weight:500;font-size:17px;color:var(--ink);margin-bottom:12px}
.feature p{font-size:10.5px;line-height:16px}
.feature-divider{left:363px;top:22px;width:1px;height:130px;background:#e4e6ee}
.more{display:flex;align-items:center;gap:14px;font-size:12px;font-weight:500;color:var(--ink);margin-top:18px}
.more span{border-bottom:1px solid var(--ink);padding-bottom:2px}

/* about */
.label{font-family:var(--head);font-size:14px;color:var(--text)}
.about-label{left:106px;top:897px}
.about-title{left:106px;top:927px;font-family:var(--head);font-weight:500;font-size:23px;color:var(--ink)}
.about-text{left:106px;top:968px;width:510px;font-size:11px;line-height:19px}
.photo{background:linear-gradient(135deg,#8aa2c0,#2c3b5e)}
.ph-cockpit{left:640px;top:880px;width:263px;height:383px;background:linear-gradient(160deg,#c9b48a 0%,#6d7b7c 35%,#23262e 70%,#7d8188 100%)}
.ph-field{left:276px;top:1072px;width:473px;height:249px;background:linear-gradient(180deg,#4e6a46 0%,#2d3f2a 35%,#1b2233 60%,#8ea36a 100%)}
.ph-hangar{left:51px;top:1138px;width:260px;height:383px;background:linear-gradient(170deg,#b9c6d6 0%,#7c95b6 40%,#1c2a48 70%,#d8dde5 100%)}
.about-text-2{left:339px;top:1389px;width:510px;font-size:11px;line-height:19px}

/* services */
.services{left:0;top:1709px;width:960px;height:574px;background:linear-gradient(180deg,var(--navy-2) 0%,#1b2150 55%,#121a45 100%)}
.services h2{left:80px;top:42px;font-family:var(--head);font-weight:500;font-size:22px;color:var(--white)}
.services .lead{left:80px;top:76px;width:420px;font-size:11px;line-height:19px;color:var(--blue-light)}
.heli-art{left:46px;top:212px;width:305px;height:303px;background:radial-gradient(ellipse at 50% 50%,#7c8aa6 0%,#2e3a5c 55%,rgba(29,35,82,0) 72%)}
.svc-card{left:594px;width:283px;height:275px;border-radius:10px;overflow:hidden;background:linear-gradient(180deg,#8fa0b8 0%,#3a4a6c 45%,#0e1a4a 72%)}
.svc-card.two{background:linear-gradient(180deg,#b08a4e 0%,#5a4a3a 40%,#0e1a4a 72%)}
.svc-card .body{left:21px;top:160px;width:240px;color:var(--white)}
.svc-card h3{font-family:var(--head);font-weight:500;font-size:15px;margin-bottom:10px}
.svc-card p{font-size:9.5px;line-height:13px;color:var(--blue-light)}
.svc-card .more{color:var(--white);font-size:11px;margin-top:8px}
.svc-card .more span{border-color:var(--blue)}

/* fleet */
.fleet-title{left:0;top:2475px;width:960px;text-align:center;font-family:var(--head);font-weight:500;font-size:22px;color:var(--ink)}
.fleet-lead{left:90px;top:2524px;width:780px;text-align:center;font-size:11px;line-height:18px}
.fleet-item{top:2636px;width:330px;height:560px}
.fleet-item .frame-v{left:0;top:0;width:2px;height:376px;background:var(--blue)}
.fleet-item .frame-h{left:0;top:374px;width:120px;height:2px;background:var(--blue)}
.fleet-item .img{left:25px;top:0;width:214px;height:354px;background:linear-gradient(180deg,#3d79c6 0%,#5a8ed0 30%,#101626 55%,#9aa0a8 80%,#c9ccd2 100%)}
.fleet-item .img.alt{background:linear-gradient(180deg,#c6d6ec 0%,#5e8048 30%,#101626 55%,#a5a59c 80%,#d0d0c8 100%)}
.fleet-item .name{left:0;top:366px;width:239px;text-align:right;font-family:var(--head);font-weight:500;font-size:15px;color:var(--ink)}
.fleet-item p{left:0;top:400px;width:245px;font-size:11px;line-height:18px}
.fleet-item .more{left:118px;top:520px;margin:0}

/* contact */
.contact{left:0;top:3226px;width:960px;height:1040px;background:var(--navy)}
.contact-photo{left:0;top:0;width:960px;height:420px;background:linear-gradient(180deg,#ffffff 0%,#c6d2e4 25%,#4c5b84 55%,#1a2456 80%,var(--navy) 100%)}
.cta{left:125px;top:3559px;width:709px;height:391px;background:var(--page);border-radius:6px 6px 40px 6px;text-align:center}
.cta .brand-cta{margin-top:56px;font-family:var(--head);font-weight:500;font-size:34px;letter-spacing:4px;color:var(--ink);display:inline-flex;align-items:center;gap:12px}
.cta .brand-cta i{width:12px;height:12px;border-radius:50%;background:var(--ink);display:inline-block}
.cta h2{margin-top:22px;font-family:var(--head);font-weight:500;font-size:30px;color:var(--ink)}
.cta .sub{margin:16px auto 0;width:420px;font-size:20px;line-height:26px;color:#7a7f8e}
.cta .line{font-family:var(--head);font-weight:500;font-size:25px;color:var(--ink);line-height:40px}
.cta .lines{margin-top:24px}
.send{left:455px;top:3922px;width:46px;height:46px;border-radius:50%;background:var(--blue);display:flex;align-items:center;justify-content:center}
.plus-grid{left:795px;top:3884px;display:grid;grid-template-columns:repeat(5,22px);row-gap:8px;color:var(--white);font-size:13px}
.plus-grid span:nth-child(5){color:#e06a5a}
.plus-grid span:nth-child(13){color:var(--blue)}
.rule{left:36px;width:888px;height:1px;background:#3a4470}
.foot-item{top:4125px;display:flex;align-items:center;gap:12px;color:var(--white);font-size:11px;line-height:17px}
.foot-item .ic{width:32px;height:32px;border-radius:50%;background:var(--white);display:flex;align-items:center;justify-content:center}
.copy{left:78px;top:4213px;font-size:9.5px;color:var(--blue-light)}
.privacy{left:794px;top:4213px;font-size:9.5px;color:var(--blue-light)}
</style>
</head>
<body>
<div class="page">

  <header class="abs header">
    <div class="abs brand"><span class="dot"></span>ROTAVIA</div>
    <nav class="abs nav"><a>Home</a><a>About Us</a><a>Services</a><a>Contact Us</a></nav>
    <div class="abs callbox">
      <svg class="abs" style="left:0;top:0" width="280" height="80" viewBox="0 0 280 80">
        <polygon points="38,0 280,0 280,80 0,80" fill="#7a86a8"/>
        <polygon points="58,0 280,0 280,80 22,80" fill="#0c1444"/>
      </svg>
      <div class="abs icon-circle" style="left:80px;top:28px">
        <svg width="14" height="14" viewBox="0 0 24 24"><path d="M6.6 10.8a15 15 0 006.6 6.6l2.2-2.2c.3-.3.7-.4 1-.2 1.1.4 2.3.6 3.6.6.6 0 1 .4 1 1V20c0 .6-.4 1-1 1A17 17 0 013 4c0-.6.4-1 1-1h3.5c.6 0 1 .4 1 1 0 1.3.2 2.5.6 3.6.1.3 0 .7-.2 1z" fill="#0c1444"/></svg>
      </div>
      <div class="abs txt">Call Us Today<br>+46 700 123 456</div>
    </div>
  </header>

  <section class="abs hero">
    <div class="abs hero-photo" role="img" aria-label="Black helicopter standing on a grass field under blue sky"></div>
    <div class="abs eyebrow">Welcome to Rotavia</div>
    <h1 class="abs">Hyr Din Helikopter Av Oss!</h1>
    <p class="abs">Lorem ipsum dolor sit amet, consectetur adipiscing elit, sed do eiusmod tempor incididunt ut labore et dolore magna aliqua. Ut enim ad minim veniam, quis nostrud exercitation ullamco</p>
    <a class="abs btn-pill">Contact US</a>
  </section>

  <div class="abs feature-card">
    <div class="abs feature" style="left:32px">
      <h3>Hyr Din Helikopter</h3>
      <p>Lorem ipsum dolor sit amet, consectetur adipiscing elit, sed do eiusmod tempor incididunt ut labore et dolore magna aliqua. Ut enim ad minim veniam, quis nostrud exercitation ullamco</p>
      <a class="more"><span>Explore Now</span><svg width="28" height="10" viewBox="0 0 28 10"><path d="M0 5h26M21 1l5 4-5 4" stroke="#111a3a" stroke-width="1.3" fill="none"/></svg></a>
    </div>
    <div class="abs feature-divider"></div>
    <div class="abs feature" style="left:413px">
      <h3>Helikopter utbildning</h3>
      <p>Lorem ipsum dolor sit amet, consectetur adipiscing elit, sed do eiusmod tempor incididunt ut labore et dolore magna aliqua. Ut enim ad minim veniam, quis nostrud exercitation ullamco</p>
      <a class="more"><span>Explore Now</span><svg width="28" height="10" viewBox="0 0 28 10"><path d="M0 5h26M21 1l5 4-5 4" stroke="#111a3a" stroke-width="1.3" fill="none"/></svg></a>
    </div>
  </div>

  <section>
    <div class="abs label about-label">About Us</div>
    <h2 class="abs about-title">Rotavia Sweden AB.</h2>
    <p class="abs about-text">Det lilla företaget med de stora möjligheterna<br>Rotavia startades med visionen att göra helikopterflygning mer tillgänglig i södra Sverige. Att flyga helikopter i sverige är oftast ganska kostsamt och svårt med tillgänglighet.</p>
    <div class="abs ph-cockpit" role="img" aria-label="Helicopter cockpit instruments with a view over the landscape"></div>
    <div class="abs ph-hangar" role="img" aria-label="Helicopter parked inside a hangar"></div>
    <div class="abs ph-field" role="img" aria-label="Black helicopter on grass in front of a forest"></div>
    <div class="abs about-text-2">
      <p>Detta medför att många som har certifikat ofta får vänta länge mellan sina flygningar. Vi vill förbättra tillgängliheten och serviecen framförallt med helikopterhyra i skåne och i södra Sverige.</p>
      <p style="margin-top:8px">Vi är några piloter som fullkomligt älskar att flyga helikopter och önskar att fler ska få kunna flyga helikopter!</p>
    </div>
  </section>

  <section class="abs services">
    <h2 class="abs">Services</h2>
    <p class="abs lead">Lorem Ipsum is simply dummy text of the printing and typesetting industry. Lorem Ipsum has been the industry's standard dummy text ever since the 1500s, when an unknown printer took a galley of type and scrambled it to make a type specimen book. It has survived not only five centuries, but also the leap into electronic typesetting, remaining essentially unchanged. It was popularised in the 1960s</p>
    <div class="abs heli-art" role="img" aria-label="Front view of a helicopter with rotor and skids"></div>
    <div class="abs svc-card" style="top:-2px" role="group">
      <div class="abs body">
        <h3>Uthyrning</h3>
        <p>Vi hyr ut helikoptrar. Vi har bland annat en helt ny Model R4 med 130 timmar på tacho.</p>
        <a class="more"><span>Read More</span><svg width="26" height="10" viewBox="0 0 26 10"><path d="M0 5h24M19 1l5 4-5 4" stroke="#0677BA" stroke-width="1.3" fill="none"/></svg></a>
      </div>
    </div>
    <div class="abs svc-card two" style="top:321px">
      <div class="abs body">
        <h3>Andra typer av helikopterjobb</h3>
        <p>Vi kan ombesörja fotoflyg, inventering av exempelvis barkborre eller vilt. Vi arbetar med Olika operatörer och utgår</p>
        <a class="more"><span>Read More</span><svg width="26" height="10" viewBox="0 0 26 10"><path d="M0 5h24M19 1l5 4-5 4" stroke="#0677BA" stroke-width="1.3" fill="none"/></svg></a>
      </div>
    </div>
  </section>

  <section>
    <h2 class="abs fleet-title">Våra Helikoptrar!</h2>
    <p class="abs fleet-lead">Vi använder oss enbart av beprövad utrustning med låga timmar och ser alltid till att de är välskötta. För oss är en ren och fräsch helikopter en förutsättning för hyran ska bli så bra som möjligt. Genom att alltid se till att allt är i toppkondition minskar vi risken för fel och onödigt slit på vårt material.</p>

    <article class="abs fleet-item" style="left:90px">
      <div class="abs frame-v"></div><div class="abs frame-h"></div>
      <div class="abs img" role="img" aria-label="Black helicopter on the apron, front three-quarter view"></div>
      <h3 class="abs name">Model R4</h3>
      <p class="abs">Helikoptern är av en säkerkonstruktion och den har energiabsorberandestolar, landningsställ och bränsletankar Helikoptrarna genomgår regelbunden service och är servade enligt konstens alla regler.</p>
      <a class="abs more"><span>Read More</span><svg width="28" height="10" viewBox="0 0 28 10"><path d="M0 5h26M21 1l5 4-5 4" stroke="#111a3a" stroke-width="1.3" fill="none"/></svg></a>
    </article>
    <article class="abs fleet-item" style="left:378px">
      <div class="abs frame-v"></div><div class="abs frame-h"></div>
      <div class="abs img alt" role="img" aria-label="Black helicopter parked in front of trees"></div>
      <h3 class="abs name">Model C2</h3>
      <p class="abs">Helikoptern är av en säkerkonstruktion och den har energiabsorberandestolar, landningsställ och bränsletankar Helikoptrarna genomgår regelbunden service och är servade enligt konstens alla regler.</p>
      <a class="abs more"><span>Read More</span><svg width="28" height="10" viewBox="0 0 28 10"><path d="M0 5h26M21 1l5 4-5 4" stroke="#111a3a" stroke-width="1.3" fill="none"/></svg></a>
    </article>
    <article class="abs fleet-item" style="left:666px">
      <div class="abs frame-v"></div><div class="abs frame-h"></div>
      <div class="abs img" role="img" aria-label="Black helicopter on the apron, front three-quarter view"></div>
      <h3 class="abs name">Model R1</h3>
      <p class="abs">Helikoptern är av en säkerkonstruktion och den har energiabsorberandestolar, landningsställ och bränsletankar Helikoptrarna genomgår regelbunden service och är servade enligt konstens alla regler.</p>
      <a class="abs more"><span>Read More</span><svg width="28" height="10" viewBox="0 0 28 10"><path d="M0 5h26M21 1l5 4-5 4" stroke="#111a3a" stroke-width="1.3" fill="none"/></svg></a>
    </article>
  </section>

  <footer class="abs contact">
    <div class="abs contact-photo" role="img" aria-label="Helicopter close-up with rotor mast against a pale sky"></div>
  </footer>

  <div class="abs cta">
    <div class="brand-cta"><i></i>ROTAVIA</div>
    <h2>Vill du hyra helikopter av oss?</h2>
    <p class="sub">Ring oss eller skicka ett mail så återkommer vi så snart som möjligt.</p>
    <div class="lines">
      <div class="line">Call Us - +46 700 123 456</div>
      <div class="line">E-mail - info@rotavia-demo.se</div>
    </div>
  </div>
  <div class="abs send">
    <svg width="20" height="20" viewBox="0 0 24 24"><path d="M21 3L3 10.5l7 2.5 2.5 7z" fill="#fff"/></svg>
  </div>
  <div class="abs plus-grid">
    <span></span><span>+</span><span>+</span><span>+</span><span>+</span>
    <span></span><span>+</span><span>+</span><span>+</span><span>+</span>
    <span></span><span>+</span><span>+</span><span>+</span><span>+</span>
    <span>+</span><span>+</span><span>+</span><span>+</span><span>+</span>
  </div>

  <div class="abs rule" style="top:4080px"></div>
  <div class="abs foot-item" style="left:78px">
    <div class="ic"><svg width="14" height="16" viewBox="0 0 24 24"><path d="M12 2a7 7 0 00-7 7c0 5 7 13 7 13s7-8 7-13a7 7 0 00-7-7zm0 9.5A2.5 2.5 0 1112 6.5a2.5 2.5 0 010 5z" fill="#0677BA"/></svg></div>
    <div>Address<br>Rotavia, Norra Flygfältet</div>
  </div>
  <div class="abs foot-item" style="left:432px">
    <div class="ic"><svg width="14" height="14" viewBox="0 0 24 24"><path d="M6.6 10.8a15 15 0 006.6 6.6l2.2-2.2c.3-.3.7-.4 1-.2 1.1.4 2.3.6 3.6.6.6 0 1 .4 1 1V20c0 .6-.4 1-1 1A17 17 0 013 4c0-.6.4-1 1-1h3.5c.6 0 1 .4 1 1 0 1.3.2 2.5.6 3.6.1.3 0 .7-.2 1z" fill="#0677BA"/></svg></div>
    <div>Phone<br>+46 700 123 456</div>
  </div>
  <div class="abs foot-item" style="left:754px">
    <div class="ic"><svg width="14" height="14" viewBox="0 0 24 24"><path d="M21 3L3 10.5l7 2.5 2.5 7z" fill="#0677BA"/></svg></div>
    <div>E-mail<br>info@rotavia-demo.se</div>
  </div>
  <div class="abs rule" style="top:4175px"></div>
  <div class="abs copy">© 2022 Rotavia LLC. ALL RIGHTS RESERVED.</div>
  <div class="abs privacy">PRIVACY POLICY</div>

</div>
</body>
</html>
```